Tidewell Works's Facebook Cover Design

I am in need of a social media cover for my company's Facebook account. Please leverage the green logos and color palette attached.

Tidewell Works offers 2 primary services:
1.) Business Automation Services
2.) AI (artificial intelligence integrations)

While a lot of what we do is highly technical, what we deliver is not. In a nutshell, we help our clients to connect their data regardless of what application that data is sitting in. Because we can connect that data, often times we can:

A.) offer more intelligent marketing and help our client increase their revenue.
B.) automate highly repetitive tasks using technology and drive down their costs thus saving them money
C.) help our clients use AI to better serve their customers

You can read a little bit about our company here: https://www.tidewellworks.example

Our tagline is: "Connect data to increase the flow of profitability."

Visually, we'd like your help to illustrate the "connecting" of these applications. Please let me know if you have any questions.

Target Market(s)

Business Owners or Marketing Managers

Industry/Entity Type

Marketing technologies.

Font styles to use
Sans Serif

Requirements
Must have
• Please make every effort to have the cover compatible with the color palette of the attached images.
Should not have
• Please do not use the standard clipart or stock libraries of AI = robot. If you do, please make them small. We help business glue their data from different sources to solve real work problems. Little robots are overused.

```html
<!DOCTYPE html>
<html lang="en">
<head>
<meta charset="utf-8">
<title>Tidewell Works — Facebook Cover</title>
<link rel="stylesheet" href="https://fonts.googleapis.com/css2?family=Red+Hat+Display:wght@400;700;900&display=swap">
<style>
  :root {
    --brand-green: #8bc53f;
    --ink-grey: #4b4b4d;
    --slate: #58595b;
    --paper: #ffffff;
    --stage: #c2c2c2;
    --line-green: #9ccf5c;
  }
  * { margin: 0; padding: 0; box-sizing: border-box; }
  html, body {
    width: 1200px; height: 1200px; overflow: hidden;
    background: var(--stage);
    font-family: "Red Hat Display", Arial, sans-serif;
  }
  .cover {
    position: absolute; left: 0; top: 372px;
    width: 1200px; height: 456px;
    background:
      radial-gradient(ellipse 420px 200px at 380px 180px, rgba(139,197,63,0.10), transparent 70%),
      radial-gradient(ellipse 360px 220px at 1050px 360px, rgba(139,197,63,0.10), transparent 70%),
      var(--paper);
    overflow: hidden;
  }
  .cover__lines { position: absolute; inset: 0; width: 100%; height: 100%; }
  .brand {
    position: absolute; left: 97px; top: 74px;
    display: flex; align-items: center; gap: 8px;
    font-weight: 700; font-size: 27px; letter-spacing: -0.5px;
    color: var(--ink-grey);
  }
  .brand__dot { width: 12px; height: 12px; border-radius: 50%; background: var(--brand-green); }
  .headline {
    position: absolute; left: 96px; top: 126px;
    font-weight: 900; font-size: 57px; line-height: 50px;
    letter-spacing: -1.2px; text-transform: uppercase;
    color: var(--brand-green);
  }
  .headline__line { display: block; white-space: nowrap; }
  .headline__line--dark { color: var(--ink-grey); }
  .services {
    position: absolute; left: 97px; top: 289px;
    color: var(--ink-grey); font-size: 22px; font-weight: 400;
  }
  .services__intro { margin-bottom: 6px; letter-spacing: -0.2px; }
  .services__list { list-style: none; }
  .services__item {
    display: flex; align-items: center; gap: 18px;
    height: 31px; padding-left: 3px;
  }
  .services__icon { width: 24px; height: 24px; flex: none; }
  .illustration {
    position: absolute; left: 729px; top: 50px;
    width: 363px; height: 365px; border-radius: 16px;
    background: linear-gradient(135deg, #58595b 0%, #6b6c6e 40%, #8bc53f 100%);
  }
</style>
</head>
<body>
  <section class="cover">
    <svg class="cover__lines" viewBox="0 0 1694 644" preserveAspectRatio="none" aria-hidden="true">
      <g fill="none" stroke="var(--line-green)" stroke-width="1.4">
        <path d="M0 241 C70 234 120 255 160 300 L502 644"/>
        <path d="M0 471 C70 468 110 490 140 524 L248 644"/>
        <path d="M1075 0 L1150 72"/>
        <path d="M1329 0 L1402 72"/>
        <path d="M1540 170 C1610 175 1660 150 1694 112"/>
        <path d="M1540 400 C1610 402 1660 370 1694 320"/>
      </g>
    </svg>

    <div class="brand"><span class="brand__name">Tidewell Works</span><span class="brand__dot"></span></div>

    <h1 class="headline">
      <span class="headline__line">Connect data to</span>
      <span class="headline__line">increase the flow</span>
      <span class="headline__line headline__line--dark">of profitability.</span>
    </h1>

    <div class="services">
      <p class="services__intro">Tidewell Works offers 2 primary services:</p>
      <ul class="services__list">
        <li class="services__item">
          <svg class="services__icon" viewBox="0 0 24 24"><circle cx="12" cy="12" r="10.5" fill="none" stroke="var(--brand-green)" stroke-width="2"/><path d="M10 7.5 L14.5 12 L10 16.5" fill="none" stroke="var(--brand-green)" stroke-width="2" stroke-linecap="round" stroke-linejoin="round"/></svg>
          <span>Business Automation Services</span>
        </li>
        <li class="services__item">
          <svg class="services__icon" viewBox="0 0 24 24"><circle cx="12" cy="12" r="10.5" fill="none" stroke="var(--brand-green)" stroke-width="2"/><path d="M10 7.5 L14.5 12 L10 16.5" fill="none" stroke="var(--brand-green)" stroke-width="2" stroke-linecap="round" stroke-linejoin="round"/></svg>
          <span>AI (artificial intelligence integrations)</span>
        </li>
      </ul>
    </div>

    <div class="illustration" role="img" aria-label="Illustration of connected app windows with a green brain, a magnifying glass with a tick, checklists and a small helper robot holding a clipboard"></div>
  </section>
</body>
</html>
```